BRINDLEWOOD MEDICAL SERVICES , stationary design

Clean , minimal , modern

Target Market(s)

Healthcare

Font styles to use
Sans Serif
Other font styles liked:
• Sans serif rounded light

Colors
b1b1b1

Requirements
Must have
• Must Have:
• - must have letter head, business card, envelope, fax sheet, id badge, folder, thank you card, notebook, invoice sheet, stamp , received stamp
• Nice to Have:
• - nice to have them all custom made (letterhead,envelope, business card, I’d badge etc
• - you need to change the logo colors , icon to dark blue and logo text to dark grey and another option with dark green icon and dark grey logo text .

```html
<!DOCTYPE html>
<html lang="en">
<head>
<meta charset="utf-8">
<title>Brindlewood Medical Services — Stationery</title>
<link rel="stylesheet" href="https://fonts.googleapis.com/css2?family=Montserrat:wght@400;500;600;700&family=Quicksand:wght@400;500&display=swap">
<style>
:root{
  --navy:#1f2a5c;
  --grey:#b1b1b1;
  --bar:#dcdcde;
  --board:#e8e8ea;
  --paper:#ffffff;
  --ink:#3a3a44;
  --panel:#e4e4e6;
}
*{box-sizing:border-box;margin:0;padding:0}
html,body{width:965px;height:1200px;overflow:hidden;background:var(--board)}
body{font-family:"Montserrat",sans-serif;color:var(--ink)}
.board{position:relative;width:1000px;height:1243px;transform:scale(.965);transform-origin:0 0}
.label{position:absolute;font-family:"Quicksand",sans-serif;font-size:19px;color:var(--navy);line-height:1.25}
.sheet{position:absolute;background:var(--paper);box-shadow:0 1px 4px rgba(0,0,0,.12)}
.logo{display:flex;align-items:center;gap:4px;color:var(--navy);font-weight:600;text-transform:uppercase;line-height:1.15;letter-spacing:.3px}
.logo .mark{width:10px;height:10px;background:var(--navy);flex:none}
.logo.light{color:#fff}.logo.light .mark{background:#fff}
.tiny{font-size:4.3px;line-height:1.55}
.small{font-size:5px;line-height:1.6}
.bar{background:var(--bar)}
.navybar{background:var(--navy);color:#fff;font-size:4.5px;font-weight:600;padding:1px 3px;text-transform:uppercase}
/* ID card */
.idcard{left:24px;top:190px;width:153px;height:228px;border-radius:8px;border:5px solid #ececee;padding:22px 10px 0;text-align:center}
.idcard .logo{justify-content:center;font-size:7px}
.photo{width:44px;height:44px;margin:24px auto 12px;background:linear-gradient(#cfd0d4,#8c8f98);border:2px solid #fff;outline:1px solid var(--navy)}
.idcard .name{font-size:7px;font-weight:700;color:var(--navy)}
.idcard .role{font-size:4.5px;margin-bottom:10px}
.idcard dl{display:grid;grid-template-columns:22px 1fr;text-align:left;font-size:4.5px;line-height:1.6;padding-left:28px}
/* Letterhead */
.letterhead{left:244px;top:94px;width:245px;height:345px;padding:28px 16px}
.letterhead .logo{font-size:6.5px;position:absolute;left:16px;top:30px}
.contact{position:absolute;font-size:4.3px;line-height:1.6}
.letterhead .contact{left:165px;top:28px}
.letter{position:absolute;left:16px;top:114px;right:16px;font-size:4.5px;line-height:1.7}
.letter .date{position:absolute;right:0;top:0}
.letter p{margin-top:10px}
.sign{width:34px;height:10px;margin:6px 0 4px;background:linear-gradient(90deg,#e2e2e4,#c9c9cc)}
/* Invoice */
.invoice{left:531px;top:77px;width:290px;height:366px;padding:14px 18px}
.invoice .logo{font-size:7px;position:absolute;left:18px;top:18px}
.invoice .contact{left:194px;top:26px}
.invoice h2{position:absolute;left:205px;top:60px;font-size:8.5px;color:var(--navy);font-weight:700}
.invoice .addr{position:absolute;left:18px;top:64px;font-size:4.3px;line-height:1.5}
.box{position:absolute;display:flex;flex-direction:column;gap:2px}
.box .bar{height:7px}
.table{position:absolute;left:18px;top:137px;width:253px}
.table .head{display:grid;grid-template-columns:22px 1fr 40px 40px;background:var(--navy);color:#fff;font-size:4.3px;font-weight:600;padding:1px 2px}
.table .row{display:grid;grid-template-columns:22px 1fr 40px 40px;gap:2px;margin-top:2px}
.table .row span{height:8px;background:var(--bar)}
.thanks{position:absolute;left:18px;top:330px;font-size:7.5px;font-weight:700;color:var(--navy)}
.terms{position:absolute;left:18px;top:343px;width:240px;font-size:3.8px;line-height:1.5}
/* Business cards */
.card{left:155px;width:112px;height:64px}
.card.front{top:469px;padding:8px}
.card.front .logo{font-size:4.5px;position:absolute;left:8px;top:20px;width:50px}
.card.front .contact{left:66px;top:14px;font-size:3.4px}
.card.back{top:550px;background:var(--navy);display:flex;align-items:center;justify-content:center}
.card.back .logo{font-size:5.5px}
.card.back .web{position:absolute;bottom:6px;width:100%;text-align:center;font-size:3.4px;color:#c9cbd6}
/* Envelopes */
.env-front{left:294px;top:481px;width:274px;height:129px}
.env-front .logo{font-size:6.5px;position:absolute;left:16px;top:24px}
.env-front .from{position:absolute;left:21px;top:90px;font-size:5px;line-height:1.5}
.window{position:absolute;left:166px;top:76px;width:92px;height:37px;background:#dedee0;border-radius:3px}
.env-back{left:593px;top:479px;width:275px;height:131px}
.env-back .flap{height:45px;background:var(--navy);display:flex;align-items:center;justify-content:center}
.env-back .logo{font-size:6px}
/* Notepad */
.notepad{left:65px;top:660px;width:200px;height:278px;padding:16px 14px}
.rings{position:absolute;left:12px;top:-9px;display:flex;gap:10.5px}
.rings i{width:3px;height:16px;border-radius:2px;background:#444}
.notepad .logo{font-size:5.5px;position:absolute;left:14px;top:18px;width:62px}
.notepad .contact{left:136px;top:14px;font-size:3.6px}
.lines{position:absolute;left:14px;right:14px;top:66px}
.lines i{display:block;height:11.2px;border-bottom:1px dashed #cfcfd2}
/* Folder */
.folder{position:absolute;left:296px;top:648px;width:580px;height:492px}
.folder svg{position:absolute;inset:0}
.folder .cover-logo{position:absolute;left:360px;top:160px;font-size:11px}
.folder .cover-logo .mark{width:16px;height:16px}
.folder .spine-logo{position:absolute;left:125px;top:292px;font-size:6.5px}
.folder .spine-info{position:absolute;left:60px;top:343px;width:170px;text-align:center;color:#fff;font-size:4.3px;line-height:1.7}
</style>
</head>
<body>
<main class="board">

  <div class="label" style="left:296px;top:54px">Letterhead design</div>
  <div class="label" style="left:606px;top:37px">Invoice design</div>
  <div class="label" style="left:30px;top:436px">Id card design</div>
  <div class="label" style="left:24px;top:520px">business card<br>design</div>
  <div class="label" style="left:880px;top:506px">envelope<br>design</div>
  <div class="label" style="left:108px;top:958px">notepad design</div>
  <div class="label" style="left:527px;top:1163px">Folder design</div>

  <!-- ID badge -->
  <section class="sheet idcard">
    <div class="logo"><span class="mark"></span><span>Brindlewood<br>Medical Services</span></div>
    <div class="photo" role="img" aria-label="Staff portrait photo"></div>
    <div class="name">DANIEL ORWELL</div>
    <div class="role">Senior Consultant</div>
    <dl>
      <dt>Id No</dt><dd>: 08254</dd>
      <dt>Email</dt><dd>: staff@brindlewoodmed.example</dd>
      <dt>Phone</dt><dd>: (555) 014-2277</dd>
      <dt>Blood</dt><dd>: (A+)</dd>
    </dl>
  </section>

  <!-- Letterhead -->
  <section class="sheet letterhead">
    <div class="logo"><span class="mark"></span><span>Brindlewood<br>Medical Services</span></div>
    <div class="contact">
      <b>brindlewood</b><br>418 Alder Row, Ste 6<br>Harlow, VA 23991<br>&#9742; +1 555 014 2880<br>&#9993; info@brindlewoodmed.example<br>&#9679; www.brindlewoodmed.example
    </div>
    <div class="letter">
      <span class="date">Date: 31/01/2019</span>
      <b>Daniel Orwell</b><br>Manager<br>56 Orchard Way<br>Millbrook, NC
      <p>Lorem ipsum dolor sit amet, consectetuer adipiscing elit, sed diam nonummy nibh euismod tincidunt ut laoreet dolore magna aliquam erat volutpat. Ut wisi enim ad minim veniam, quis nostrud exerci tation ullamcorper suscipit lobortis nisl ut aliquip ex ea commodo consequat. Lorem ipsum dolor sit amet, consectetuer adipiscing elit, sed diam nonummy nibh euismod tincidunt ut laoreet dolore magna aliquam erat volutpat. Ut wisi enim ad minim veniam, quis nostrud exerci tation ullamcorper suscipit lobortis nisl ut aliquip ex ea commodo consequat.</p>
      <p>Consequat. Duis autem vel eum iriure dolor in hendrerit in vulputate velit esse molestie consequat, vel illum dolore eu feugiat nulla facilisis at vero eros et accumsan.</p>
      <p>sincerely</p>
      <div class="sign" role="img" aria-label="Handwritten signature"></div>
      Lena Harwick
    </div>
  </section>

  <!-- Invoice -->
  <section class="sheet invoice">
    <div class="logo"><span class="mark"></span><span>Brindlewood<br>Medical Services</span></div>
    <div class="contact">&#9742; +1 555 014 2880<br>&#9993; info@brindlewoodmed.example<br>&#9679; www.brindlewoodmed.example</div>
    <h2>INVOICE</h2>
    <div class="addr">Invoice No.1<br>Street Name Avenue, Suite<br>100 State, Zip Code, Country</div>
    <div class="box" style="left:18px;top:87px;width:89px"><div class="navybar">From :</div><div class="bar"></div><div class="bar"></div><div class="bar"></div></div>
    <div class="box" style="left:181px;top:87px;width:89px"><div class="navybar">To :</div><div class="bar"></div><div class="bar"></div><div class="bar"></div></div>
    <div class="table">
      <div class="head"><span>S.NO.</span><span style="text-align:center">DESCRIPTION</span><span>UNIT PRICE</span><span>AMOUNT</span></div>
      <div class="row"><span></span><span></span><span></span><span></span></div>
      <div class="row"><span></span><span></span><span></span><span></span></div>
      <div class="row"><span></span><span></span><span></span><span></span></div>
      <div class="row"><span></span><span></span><span></span><span></span></div>
      <div class="row"><span></span><span></span><span></span><span></span></div>
      <div class="row"><span></span><span></span><span></span><span></span></div>
      <div class="row"><span></span><span></span><span></span><span></span></div>
      <div class="row"><span></span><span></span><span></span><span></span></div>
    </div>
    <div class="box" style="left:18px;top:249px;width:82px"><div class="navybar">Payment methods</div><div class="small" style="padding-left:4px">Bank Name :<br>A/C Name :<br>Account No :</div></div>
    <div class="box" style="left:190px;top:249px;width:81px"><div class="navybar" style="text-align:center">Amount due</div><div class="bar"></div><div class="bar"></div><div class="bar"></div></div>
    <div style="position:absolute;left:198px;top:306px;width:70px;text-align:center;font-size:5px;color:var(--navy)">
      <div class="sign" role="img" aria-label="Handwritten signature" style="margin:0 auto 2px;width:60px"></div><b>Lena Harwick</b><br><span style="font-size:3.5px">Account Manager</span>
    </div>
    <div class="thanks">Thank you for your business!</div>
    <div class="terms"><b style="color:var(--navy)">TERMS &amp; CONDITIONS</b> : Payment is due within thirty days of the invoice date. Please quote the invoice number with every transfer so it can be matched promptly.</div>
  </section>

  <!-- Business cards -->
  <section class="sheet card front">
    <div class="logo"><span class="mark" style="width:7px;height:7px"></span><span>Brindlewood<br>Medical Services</span></div>
    <div class="contact"><b>Daniel Orwell</b><br>Senior Consultant<br>418 Alder Row, Ste 6<br>Harlow, VA 23991<br>&#9742; +1 555 014 2880<br>&#9993; info@brindlewoodmed.example<br>&#9679; brindlewoodmed.example</div>
  </section>
  <section class="sheet card back">
    <div class="logo light"><span class="mark" style="width:8px;height:8px"></span><span>Brindlewood<br>Medical Services</span></div>
    <div class="web">www.brindlewoodmed.example</div>
  </section>

  <!-- Envelopes -->
  <section class="sheet env-front">
    <div class="logo"><span class="mark"></span><span>Brindlewood<br>Medical Services</span></div>
    <div class="from"><b style="color:var(--navy)">brindlewood</b><br>418 Alder Row, Ste 6<br>Harlow, VA 23991</div>
    <div class="window"></div>
  </section>
  <section class="sheet env-back">
    <div class="flap"><div class="logo light"><span class="mark"></span><span>Brindlewood</span></div></div>
  </section>

  <!-- Notepad -->
  <section class="sheet notepad">
    <div class="rings"><i></i><i></i><i></i><i></i><i></i><i></i><i></i><i></i><i></i><i></i><i></i><i></i><i></i><i></i></div>
    <div class="logo"><span class="mark" style="width:8px;height:8px"></span><span>Brindlewood<br>Medical Services</span></div>
    <div class="contact"><b>brindlewood</b><br>418 Alder Row, Ste 6<br>Harlow, VA 23991<br>&#9742; +1 555 014 2880<br>&#9993; info@brindlewoodmed.example<br>&#9679; brindlewoodmed.example</div>
    <div class="lines"><i></i><i></i><i></i><i></i><i></i><i></i><i></i><i></i><i></i><i></i><i></i><i></i><i></i><i></i><i></i><i></i><i></i><i></i></div>
  </section>

  <!-- Presentation folder -->
  <section class="folder">
    <svg width="580" height="492" viewBox="0 0 580 492" aria-hidden="true">
      <path d="M6 0H290V336H6V198a14 14 0 0 0 0-28Z" fill="var(--navy)"/>
      <rect x="290" y="0" width="265" height="336" fill="var(--panel)"/>
      <path d="M555 4L580 14V170a14 14 0 0 0 0 28V358L555 368Z" fill="var(--navy)"/>
      <path d="M6 336H555L580 358V370L560 380V480a12 12 0 0 1-12 12H300a10 10 0 0 1-10-10V392a22 22 0 0 0-22-22H36a12 12 0 0 1-12-12V336Z" fill="var(--navy)"/>
      <rect x="24" y="336" width="266" height="156" rx="10" fill="var(--navy)"/>
      <line x1="367" y1="412" x2="382" y2="398" stroke="#3a4680" stroke-width=".8"/>
      <line x1="462" y1="463" x2="477" y2="448" stroke="#3a4680" stroke-width=".8"/>
    </svg>
    <div class="logo cover-logo"><span class="mark"></span><span>Brindlewood<br>Medical Services</span></div>
    <div class="logo light spine-logo"><span class="mark" style="width:8px;height:8px"></span><span>Brindlewood<br>Medical Services</span></div>
    <div class="spine-info">Level 2, 14 Fernhill Lane, Harlow, VA 23991<br>&#9742; 555-0188 &nbsp; &#9742; 555-0176 &nbsp; &#9679; www.brindlewoodmed.example</div>
  </section>

</main>
</body>
</html>
```